Structural Engineering Firm Looking for High-Impact Lead Generation Focused Design (for B2B)

A well-established structural engineering firm in the UK wants a new website designed for them which will help them realise more business from online. Directly through the website as well as Ads and lead platforms. They need to compare favourably to competitors and have clarity. Current Site is here: http://www.marlowgrantpartners.example/ - you can take imagery from this site if you want to help with the design.
Updates

Target Market(s)

Homeowners, Architects, Designers, Construction Companies and Landlords

Industry/Entity Type

Professional Services

Number of Pages Required

5+ page

Font styles to use
Sans Serif

Requirements
Must have
• A Strong, Simple and Professional Design with a Focus on Lead Generation
Nice to have
• Creativity in the Detail, Clear Messaging
Should not have
• Too Much Colour, Too 'Consumer', Too Much Variation

```html
<!DOCTYPE html>
<html lang="en">
<head>
<meta charset="utf-8">
<title>Marlow Grant Partners – Structural Engineering &amp; Party Wall Surveying</title>
<link href="https://fonts.googleapis.com/css2?family=Oswald:wght@400;500&family=Arimo:wght@400;700&display=swap" rel="stylesheet">
<style>
:root{
  --orange:#f07f5a;
  --teal:#a9c8bf;
  --ink:#1c1c1c;
  --dark:#2b2b2b;
  --grey:#8a8a8a;
  --white:#ffffff;
}
*{box-sizing:border-box;margin:0;padding:0}
html,body{width:1200px;height:4286px;overflow:hidden;background:var(--white)}
body{position:relative;font-family:"Arimo",Arial,sans-serif;color:var(--ink)}
.abs{position:absolute}
.display{font-family:"Oswald",sans-serif;font-weight:500;text-transform:uppercase;letter-spacing:.5px}
.copy{font-size:14px;line-height:24px;color:var(--grey);text-align:justify}

/* top bar */
.topbar{left:0;top:0;width:1200px;height:43px;background:#0d0d0d;font-size:14px;color:#fff;white-space:nowrap}
.topbar .phone{left:97px;top:0;width:286px;height:43px;background:var(--orange);padding:13px 14px;font-size:13px}
.topbar .mail{left:383px;top:0;width:249px;height:43px;background:var(--teal);padding:13px 10px;font-size:12.5px;overflow:hidden}
.topbar .links{right:110px;top:12px;font-size:14px;word-spacing:4px}

/* nav */
.nav{left:0;top:43px;width:1200px;height:90px;background:#fff}
.logo{left:111px;top:18px;font-family:"Arimo",sans-serif;font-size:29px;line-height:26px;color:var(--ink);letter-spacing:-.5px}
.menu{left:366px;top:44px;display:flex;gap:26px;font-size:13.5px;font-weight:700;color:var(--ink);white-space:nowrap}
.menu .active{color:var(--orange);position:relative}
.menu .active::before{content:"";position:absolute;left:0;right:0;top:-12px;height:3px;background:var(--orange)}
.menu .plus{color:var(--orange)}

/* hero */
.hero{left:0;top:133px;width:1200px;height:617px;background:linear-gradient(180deg,#3b4a63 0%,#59606a 35%,#4a4640 70%,#2a2622 100%)}
.hero-frame{left:91px;top:325px;width:240px;height:213px;border:5px solid var(--orange);border-right:none}
.hero-title{left:110px;top:338px;font-size:53px;line-height:60px;color:#fff;font-weight:400;white-space:nowrap}
.dots{left:1137px;top:394px}
.dots span{display:block;width:12px;height:12px;transform:rotate(45deg);background:#fff;margin-bottom:16px}
.dots span:first-child{background:var(--orange)}
.scroll-mark{left:113px;top:666px}

/* quote */
.quote-teal{left:985px;top:750px;width:215px;height:292px;background:var(--teal)}
.quote{left:0;top:750px;width:985px;height:258px;background:var(--orange)}
.quote h2{position:absolute;left:0;width:1200px;top:56px;text-align:center;font-size:37px;line-height:40px;color:#fff}
.select{background:#fff;border:1px solid #ddd;font-size:13.5px;color:#555;padding:0 20px;display:flex;align-items:center;justify-content:space-between}
.quote .select{position:absolute;left:313px;top:155px;width:574px;height:45px}

/* intro rows */
.frame-black{border:8px solid var(--ink)}
.photo{overflow:hidden}
h2.sec{font-size:36px;line-height:43px;color:var(--ink);white-space:nowrap}

/* steps */
.steps-dark{left:0;top:2112px;width:602px;height:532px;background:linear-gradient(135deg,#3a3a3a,#1e1e1e 60%,#2e2e2e)}
.steps-frame{left:97px;top:2218px;width:286px;height:212px;border:5px solid #fff;border-right:none}
.steps-title{left:122px;top:2230px;font-size:40px;line-height:60px;color:#fff;font-weight:500;white-space:nowrap}
.btn{border:1px solid var(--orange);color:var(--orange);font-size:13px;font-weight:700;display:flex;align-items:center;justify-content:center;white-space:nowrap}
.tile{width:299px;height:266px;display:flex;flex-direction:column;align-items:center;padding-top:74px;color:#fff;font-weight:700;font-size:20px}
.tile svg{margin-bottom:30px}
.t-orange{background:var(--orange)}
.t-teal{background:var(--teal)}

/* projects */
.proj-dark{left:597px;top:3208px;width:603px;height:659px;background:linear-gradient(135deg,#3a3a3a,#1d1d1d 50%,#333)}
.proj-orange{left:0;top:3277px;width:805px;height:658px;background:var(--orange)}
.proj-frame{left:113px;top:3341px;width:330px;height:165px;border:5px solid #fff;border-right:none}
.proj-title{left:136px;top:3356px;font-size:36px;line-height:43px;color:#fff;font-weight:500;white-space:nowrap}
.card{top:3548px;width:233px;height:269px;background:#fff;padding:22px 28px}
.card h3{font-size:15px;font-weight:700;margin:16px 0 12px}
.card p{font-size:13px;line-height:25px;color:var(--grey)}
.card .btn{width:108px;height:34px;margin-top:14px;color:var(--ink);font-size:13px}

/* partnership */
.partner{left:0;top:3935px;width:1200px;height:351px;background:linear-gradient(180deg,#fff,#f4f4f4)}
.partner h2{position:absolute;left:0;width:1200px;top:88px;text-align:center;font-size:37px}
.partner p{position:absolute;left:213px;width:774px;top:135px;font-size:14px;line-height:26px;color:var(--grey);text-align:center}
</style>
</head>
<body>

<!-- top bar -->
<div class="abs topbar">
  <div class="abs phone">&#9990; Call us Today : +44 (0) 20 7946 0321</div>
  <div class="abs mail">&#9993; info@marlowgrantpartners.example</div>
  <div class="abs links">Gallery &nbsp;| &nbsp;Blog &nbsp;| &nbsp;About Us &nbsp;| &nbsp;Contact Us</div>
</div>

<!-- navigation -->
<div class="abs nav">
  <div class="abs logo">MARLOW GRANT<br>PARTNERS</div>
  <div class="abs menu">
    <span class="active">HOME</span>
    <span>STRUCTURAL DESIGN<span class="plus">+</span></span>
    <span>STRUCTURAL SURVEYS</span>
    <span>PLANNING<span class="plus">+</span></span>
    <span>PARTY WALL<span class="plus">+</span></span>
    <span>PARTNERS</span>
  </div>
</div>

<!-- hero -->
<div class="abs hero" role="img" aria-label="Photo of a renovated brick townhouse courtyard at dusk"></div>
<div class="abs hero-frame"></div>
<div class="abs display hero-title">Efficint &amp; Professional<br>Structural Engineering<br>&amp; Party Wall Surveying</div>
<div class="abs dots"><span></span><span></span><span></span><span></span></div>
<svg class="abs scroll-mark" width="38" height="110" viewBox="0 0 38 110">
  <rect x="6" y="6" width="26" height="26" transform="rotate(45 19 19)" fill="none" stroke="#fff" stroke-width="1.5"/>
  <path d="M14 17l5 5 5-5" fill="none" stroke="#fff" stroke-width="1.5"/>
  <line x1="19" y1="40" x2="19" y2="110" stroke="#fff" stroke-width="1.5"/>
</svg>

<!-- quote -->
<div class="abs quote-teal"></div>
<div class="abs quote">
  <h2 class="display">Get a Completitive Quote from<br>the Local Experts</h2>
  <div class="select"><span>What Services Are you Looking for?</span><span>&#8964;</span></div>
</div>

<!-- structural engineers -->
<div class="abs frame-black" style="left:111px;top:1098px;width:445px;height:433px"></div>
<div class="abs photo" style="left:141px;top:1123px;width:445px;height:435px;background:linear-gradient(160deg,#6d8aa6,#b9c3c7 40%,#8b6a4d 65%,#3c3c3c)" role="img" aria-label="Photo of a modern white and timber-clad house"></div>
<h2 class="abs display sec" style="left:637px;top:1088px">Structural Engineers<br>in London and the<br>South East</h2>
<p class="abs copy" style="left:637px;top:1230px;width:450px">Lorem ipsum dolor sit amet, consectetur adipiscing elit, sed do eiusmod tempor incididunt ut labore et dolore magna aliqua. Ut enim ad minim veniam, quis nostrud exercitation ullamco laboris nisi ut aliquip ex ea commodo consequat. Duis aute irure dolor in reprehenderit in voluptate velit esse cillum dolore eu fugiat nulla pariatur.</p>
<p class="abs copy" style="left:637px;top:1398px;width:450px">Excepteur sint occaecat cupidatat non proident, sunt in culpa qui officia deserunt mollit anim id est laborum. Lorem ipsum dolor sit amet, consectetur adipiscing elit, sed do eiusmod tempor incididunt ut labore et dolore magna aliqua. Ut enim ad minim</p>

<!-- party wall -->
<h2 class="abs display sec" style="left:111px;top:1628px">Choose the Party Wall<br>Specialists</h2>
<p class="abs copy" style="left:111px;top:1730px;width:450px">Lorem ipsum dolor sit amet, consectetur adipiscing elit, sed do eiusmod tempor incididunt ut labore et dolore magna aliqua. Ut enim ad minim veniam, quis nostrud exercitation ullamco laboris nisi ut aliquip ex ea commodo consequat. Duis aute irure dolor in reprehenderit in voluptate velit esse cillum dolore eu fugiat nulla pariatur.</p>
<p class="abs copy" style="left:111px;top:1898px;width:450px">Excepteur sint occaecat cupidatat non proident, sunt in culpa qui officia deserunt mollit anim id est laborum. Lorem ipsum dolor sit amet, consectetur adipiscing elit, sed do eiusmod tempor incididunt ut labore et dolore magna aliqua. Ut enim ad minim</p>
<div class="abs frame-black" style="left:646px;top:1558px;width:444px;height:432px"></div>
<div class="abs photo" style="left:616px;top:1583px;width:444px;height:435px;background:linear-gradient(120deg,#9a6a4c,#c49a7a 35%,#e6e2da 60%,#8a6a4a)" role="img" aria-label="Photo of a dining room with exposed brick wall and timber table"></div>

<!-- steps -->
<div class="abs steps-dark" role="img" aria-label="Dark photo of a modern interior staircase"></div>
<div class="abs steps-frame"></div>
<div class="abs display steps-title">From Drawing &nbsp;to<br>Delivered we Support<br>you every step of the way</div>
<div class="abs btn" style="left:105px;top:2474px;width:148px;height:47px">FIND OUT MORE</div>

<div class="abs tile t-orange" style="left:602px;top:2112px">
  <svg width="80" height="90" viewBox="0 0 80 90" fill="none" stroke="#fff" stroke-width="2.5"><rect x="8" y="10" width="52" height="74" rx="3"/><rect x="24" y="4" width="20" height="10" rx="2"/><path d="M16 34h10M16 48h10M16 62h10M32 34h14M32 48h14M32 62h14"/><circle cx="62" cy="26" r="12"/><path d="M56 26l5 5 8-9"/></svg>
  BRIEF
</div>
<div class="abs tile t-teal" style="left:902px;top:2112px">
  <svg width="92" height="90" viewBox="0 0 92 90" fill="none" stroke="#fff" stroke-width="2.5"><rect x="6" y="12" width="72" height="64"/><path d="M6 76l10 8h72V20l-10-8"/><path d="M26 60l40-40 8 8-40 40-10 2z"/><path d="M58 70l20-20v20z"/></svg>
  DESIGN
</div>
<div class="abs tile t-teal" style="left:602px;top:2378px">
  <svg width="86" height="92" viewBox="0 0 86 92" fill="none" stroke="#fff" stroke-width="2.5"><rect x="6" y="8" width="56" height="76" rx="3"/><rect x="22" y="2" width="24" height="10" rx="2"/><circle cx="34" cy="46" r="16"/><path d="M27 46l5 5 9-9"/><path d="M46 58l24 24"/></svg>
  REFINE
</div>
<div class="abs tile t-orange" style="left:902px;top:2378px">
  <svg width="112" height="80" viewBox="0 0 112 80" fill="none" stroke="#fff" stroke-width="2.5"><path d="M10 10h60v48H10z"/><path d="M70 24h20l14 16v18H70z"/><circle cx="28" cy="64" r="9"/><circle cx="88" cy="64" r="9"/><path d="M28 32l8 8 16-16"/><path d="M2 30h12M2 42h12"/></svg>
  DELIVER
</div>

<!-- fast turnaround -->
<div class="abs" style="left:115px;top:2757px;width:482px;height:520px;background:var(--teal)"></div>
<div class="abs photo" style="left:136px;top:2732px;width:443px;height:476px;background:linear-gradient(180deg,#f2f0eb,#d9d6cf 50%,#3a3a3a)" role="img" aria-label="Photo of floating white stair treads beside a dark wall"></div>
<h2 class="abs display sec" style="left:636px;top:2738px">Need a Fast Turnaround?</h2>
<p class="abs copy" style="left:636px;top:2790px;width:450px">Lorem ipsum dolor sit amet, consectetur adipiscing elit, sed do eiusmod tempor incididunt ut labore et dolore magna aliqua. Ut enim ad minim veniam, quis nostrud exercitation ullamco laboris nisi ut aliquip ex ea commodo consequat. Duis aute irure dolor in reprehenderit in voluptate velit esse cillum dolore eu fugiat nulla pariatur.</p>
<div class="abs" style="left:626px;top:2962px;width:460px;height:1px;background:var(--orange)"></div>
<div class="abs" style="left:1086px;top:2962px;width:1px;height:50px;background:var(--orange)"></div>
<div class="abs select" style="left:636px;top:2966px;width:454px;height:44px">
  <span>What Services Are you Looking for?</span><span>&#8964;</span>
</div>
<p class="abs copy" style="left:636px;top:3048px;width:450px">Excepteur sint occaecat cupidatat non proident, sunt in culpa qui officia deserunt mollit anim id est laborum. Lorem ipsum dolor sit amet, consectetur adipiscing elit, sed do eiusmod tempor incididunt ut</p>

<!-- projects -->
<div class="abs proj-dark" role="img" aria-label="Dark photo of a contemporary building interior"></div>
<div class="abs proj-orange"></div>
<div class="abs proj-frame"></div>
<div class="abs display proj-title">We have delivered over 2,000<br>engineering projects, here are some<br>of our favourites</div>

<div class="abs card" style="left:111px">
  <svg width="58" height="58" viewBox="0 0 58 58" fill="none" stroke="var(--orange)" stroke-width="2"><rect x="4" y="14" width="40" height="40"/><path d="M14 44l30-30 6 6-30 30-8 2z"/></svg>
  <h3>ASHCOMBE</h3><p>Lorem ipsum dolor sit ame tconsectetur adipiscing eli sed do</p>
  <div class="btn">READ MORE</div>
</div>
<div class="abs card" style="left:359px">
  <svg width="58" height="58" viewBox="0 0 58 58" fill="none" stroke="var(--orange)" stroke-width="2"><path d="M6 54V28L28 10l22 18v26z"/><rect x="22" y="36" width="12" height="18"/></svg>
  <h3>LARKFIELD HOUSE</h3><p>Lorem ipsum dolor sit ame tconsectetur adipiscing eli sed do</p>
  <div class="btn">READ MORE</div>
</div>
<div class="abs card" style="left:607px">
  <svg width="58" height="58" viewBox="0 0 58 58" fill="none" stroke="var(--orange)" stroke-width="2"><rect x="6" y="24" width="46" height="30"/><circle cx="18" cy="14" r="7"/><circle cx="38" cy="14" r="7"/><path d="M14 38h30"/></svg>
  <h3>THORNBURY</h3><p>Lorem ipsum dolor sit ame tconsectetur adipiscing eli sed do</p>
  <div class="btn">READ MORE</div>
</div>
<div class="abs card" style="left:855px">
  <svg width="58" height="58" viewBox="0 0 58 58" fill="none" stroke="var(--orange)" stroke-width="2"><path d="M4 40c14-10 34-10 50 0M4 50c14-10 34-10 50 0"/><circle cx="38" cy="16" r="8"/><path d="M38 24v12"/></svg>
  <h3>ELM RIDGE</h3><p>Lorem ipsum dolor sit ame tconsectetur adipiscing eli sed do</p>
  <div class="btn">READ MORE</div>
</div>

<!-- partnership -->
<div class="abs partner">
  <h2 class="display">We Work in Partnership</h2>
  <p>Lorem ipsum dolor sit amet, consectetur adipiscing elit, sed do eiusmod tempor incididunt ut labore et dolore magna aliqua. Ut enim ad minim veniam, quis nostrud exercitation ullamco laboris nisi ut aliquip ex ea commodo consequat. Duis aute irure dolor in reprehenderit in voluptate velit esse cillum dolore eu fugiat nulla pariatur. Excepteur sint occaecat cupidatat non proident, sunt in culpa qui officia deserunt mollit anim id est laborum.</p>
</div>
<div class="abs btn" style="left:369px;top:4190px;width:167px;height:42px">PARTNER WITH US</div>
<div class="abs btn" style="left:576px;top:4190px;width:246px;height:42px">INTRODUCE US TO YOUR TEAM</div>

</body>
</html>
```